Restaurant needs a vertical banner for fried catfish

Our restaurant is looking for an eye-catching 78.75in. x 36in. vertical physical banner ad for our fried catfish. Photos for the fried catfish will be provided as a reference but we will also accept anything similar to the photo. We will be using the following as our receptacle: https://www.plankoria.example/banner-stand/retractable-banner-stands/
The design must incorporate the following flavor texts:
Fried Catfish
Always Fresh!
Made from Scratch
Hand-cut Fillets
The Best Catfish in Texas
Served with fries, hush puppies, and a 32oz fountain drink
Also available by the pound!
The final design should be creative, professional, and eye-catching for customers.
Updates
Colors
Designer to choose colors to be used in the design.
Requirements
Must have
- We are open to any and all design elements, albeit the 'flavor texts' should not overpower, but complement the fried catfish photo. 'Fried Catfish' can be used in lieu of a main title/logo.
Nice to have
- Transparent or textured backgrounds that can encompass any or all part of the banner such as a cutting board, shadows, abstract, etc to show depth are a plus.
- Use of vectors or objects such as ribbons or shapes to encapsulate the 'flavor texts' are also encouraged.

```html
<!DOCTYPE html>
<html lang="en">
<head>
<meta charset="UTF-8">
<title>Fried Catfish Banner</title>
<link href="https://fonts.googleapis.com/css2?family=Luckiest+Guy&family=Bebas+Neue&family=Courier+Prime:wght@700&display=swap" rel="stylesheet">
<style>
  :root {
    --bg: #d9d9d9;
    --orange: #ff6a00;
    --orange-light: #ffa200;
    --ring: #ff7a00;
    --yellow: #ffc400;
    --red: #e30613;
    --ink: #111111;
    --white: #ffffff;
    --photo-dark: #8a4a12;
    --photo-mid: #c77a22;
    --photo-light: #e8a84a;
  }
  * { box-sizing: border-box; margin: 0; padding: 0; }
  html, body { width: 1200px; height: 1200px; overflow: hidden; background: var(--bg); }
  .banner {
    position: absolute;
    left: 340px; top: 30px;
    width: 520px; height: 1140px;
    overflow: hidden;
    background: var(--white);
  }
  .banner-backdrop {
    position: absolute; inset: 0;
    background:
      radial-gradient(ellipse at 20% 6%, #9fb35a 0 6%, transparent 14%),
      radial-gradient(ellipse at 55% 5%, #d9542a 0 8%, transparent 18%),
      radial-gradient(ellipse at 30% 40%, var(--photo-light) 0 10%, transparent 30%),
      radial-gradient(ellipse at 75% 60%, var(--photo-light) 0 8%, transparent 28%),
      linear-gradient(180deg, #b86a20 0%, var(--photo-mid) 30%, var(--photo-dark) 55%, var(--photo-mid) 78%, #f2e6d6 92%, var(--white) 100%);
  }
  .title {
    position: absolute; left: 0; right: 0;
    text-align: center;
    font-family: "Luckiest Guy", sans-serif;
    color: var(--orange);
    -webkit-text-stroke: 2px var(--white);
    paint-order: stroke fill;
    text-shadow: 0 0 0 var(--white), 3px 3px 0 var(--white), 7px 7px 0 #2a1a10;
    line-height: 1;
  }
  .title-fried { top: 60px; font-size: 98px; padding-left: 10px; }
  .title-catfish { top: 150px; font-size: 118px; letter-spacing: -2px; }
  .tagline {
    position: absolute; left: 70px; width: 380px; top: 300px; height: 50px;
    background: var(--yellow);
    clip-path: polygon(0 0, 100% 0, 96% 50%, 100% 100%, 0 100%, 4% 50%);
    font-family: "Bebas Neue", sans-serif; font-size: 40px; letter-spacing: 2px;
    color: var(--ink); text-align: center; line-height: 54px;
    transform: rotate(-1deg);
  }
  .dish {
    position: absolute; left: 65px; top: 368px;
    width: 390px; height: 390px; border-radius: 50%;
    border: 12px solid var(--ring);
    background:
      radial-gradient(circle at 70% 18%, #d94a2a 0 8%, transparent 12%),
      radial-gradient(circle at 80% 45%, #f4f1ea 0 10%, transparent 14%),
      radial-gradient(ellipse at 25% 85%, #f3c45a 0 18%, transparent 30%),
      linear-gradient(135deg, #c47a26 0%, #a55a18 45%, #d49238 70%, #f4efe6 100%);
  }
  .ribbon {
    position: absolute; height: 62px;
    background: var(--red);
    clip-path: polygon(0 0, 100% 0, 95% 50%, 100% 100%, 0 100%, 5% 50%);
    font-family: "Bebas Neue", sans-serif; font-size: 44px;
    color: var(--white); text-align: center; line-height: 68px;
  }
  .ribbon-scratch { left: 60px; width: 410px; top: 778px; transform: rotate(-2deg); }
  .ribbon-fillets { left: 85px; width: 360px; top: 848px; transform: rotate(-2deg); }
  .ribbon-best { left: 40px; width: 450px; top: 920px; transform: rotate(-2deg); font-size: 42px; }
  .served {
    position: absolute; left: 40px; right: 40px; top: 992px;
    font-family: "Courier Prime", monospace; font-size: 21px; line-height: 1.1;
    color: var(--white); text-align: center;
    text-shadow: 1px 1px 2px rgba(0,0,0,0.4);
    transform: rotate(-2deg);
  }
  .by-pound {
    position: absolute; left: 65px; width: 410px; top: 1062px; height: 46px;
    background: var(--yellow);
    font-family: "Courier Prime", monospace; font-size: 21px;
    color: var(--ink); text-align: center; line-height: 46px;
    transform: rotate(-2deg);
  }
</style>
</head>
<body>
  <main class="banner">
    <div class="banner-backdrop" role="img" aria-label="Blurred close-up of fried catfish and fries"></div>
    <div class="title title-fried">FRIED</div>
    <div class="title title-catfish">CATFISH</div>
    <div class="tagline">Always Fresh!</div>
    <div class="dish" role="img" aria-label="Plate of cornmeal-fried catfish fillets with fries, hush puppies, tartar sauce and tomato"></div>
    <div class="ribbon ribbon-scratch">MADE FROM SCRATCH</div>
    <div class="ribbon ribbon-fillets">HAND-CUT FILLETS</div>
    <div class="ribbon ribbon-best">THE BEST CATFISH IN TEXAS</div>
    <p class="served">Served with fries, hush puppies,<br>and a 32oz fountain drink</p>
    <div class="by-pound">Also available by the pound!</div>
  </main>
</body>
</html>
```